Brindle Capital and Investments

Create a simple business card design using the logos attached. Make it similar but not exact to the reference photo. Brand guidelines are also included.

```html
<!DOCTYPE html>
<html lang="en">
<head>
<meta charset="utf-8">
<title>Brindle Capital – Business Card</title>
<link href="https://fonts.googleapis.com/css2?family=Montserrat:wght@700&family=Poppins:wght@400;500;600&display=swap" rel="stylesheet">
<style>
  :root {
    --backdrop: #3a3b3d;
    --paper: #ffffff;
    --navy: #1f2a44;
    --navy-soft: #2a3656;
    --copper: #a85a24;
    --ink: #1c1c1c;
  }
  * { margin: 0; padding: 0; box-sizing: border-box; }
  html, body { width: 1200px; height: 1200px; overflow: hidden; }
  body {
    background: var(--backdrop);
    font-family: "Poppins", sans-serif;
    display: flex;
    flex-direction: column;
    align-items: center;
    justify-content: center;
    gap: 70px;
  }
  .card {
    position: relative;
    width: 840px;
    height: 480px;
    border-radius: 34px;
    border-bottom: 5px solid var(--copper);
    overflow: hidden;
  }
  .card-front { background: var(--paper); }
  .card-back { background: var(--navy); }

  .brand-name {
    font-family: "Poppins", sans-serif;
    font-weight: 600;
    text-transform: uppercase;
    letter-spacing: 6px;
    display: flex;
    align-items: center;
    gap: 14px;
  }
  .brand-dot {
    width: 14px; height: 14px; border-radius: 50%;
    background: var(--copper);
  }
  .card-front .brand-name {
    position: absolute; left: 50%; top: 90px;
    transform: translateX(-50%);
    font-size: 34px; color: var(--navy);
  }

  .holder-name {
    position: absolute; left: 62px; top: 250px;
    font-family: "Montserrat", sans-serif; font-weight: 700;
    font-size: 40px; color: var(--copper); line-height: 1;
  }
  .holder-title {
    position: absolute; left: 64px; top: 296px;
    font-size: 22px; color: var(--ink); letter-spacing: 1px;
  }
  .divider {
    position: absolute; left: 62px; right: 62px; top: 332px;
    height: 1.5px; background: var(--copper);
  }
  .contact-list {
    position: absolute; left: 64px; top: 346px;
    list-style: none; font-size: 20px; line-height: 1.4; color: var(--ink);
  }
  .contact-label { color: var(--copper); }
  .address {
    position: absolute; right: 62px; top: 262px;
    font-size: 21px; line-height: 1.3; color: var(--ink); text-align: right;
  }

  .pattern-field {
    position: absolute; inset: 0;
    background: radial-gradient(circle at 50% 50%, var(--navy-soft), var(--navy) 75%);
  }
  .card-back .brand-name {
    position: absolute; left: 50%; top: 50%;
    transform: translate(-50%, -50%);
    font-size: 34px; color: #ffffff;
  }
</style>
</head>
<body>
  <section class="card card-front">
    <div class="brand-name"><span class="brand-dot"></span>Brindle Capital</div>
    <div class="holder-name">FULL NAME</div>
    <div class="holder-title">TITLE</div>
    <div class="address">123 Name Street, 000<br>Your City, 00000-000</div>
    <div class="divider"></div>
    <ul class="contact-list">
      <li>email@company.com</li>
      <li><span class="contact-label">Direct</span> 111 000 0000</li>
      <li><span class="contact-label">Cell</span> 111 000 0000</li>
    </ul>
  </section>

  <section class="card card-back">
    <div class="pattern-field" role="img" aria-label="Subtle embossed repeating brand pattern on navy"></div>
    <div class="brand-name"><span class="brand-dot"></span>Brindle Capital</div>
  </section>
</body>
</html>
```